Brisket Dwelling Review is a leading provider of residential appraisal and home inspection products in S

I need a business card/logo designed that obviously describes my business. We are a residential appraisal and home inspection company in Springfield, MO. We offer residential appraisals, home inspection, pest inspection and radon gas measurement. We have been in business for 18 years and hold state certified residential appraisal licenses and VORMEL certified home inspection licenses. I have a logo that I really like and will attach, but would be open to new suggestions. I like more modern designs than traditional and would like a two sided card with our services, licenses and qualifications on the back.

```html
<!DOCTYPE html>
<html lang="en">
<head>
<meta charset="utf-8">
<title>Brisket Dwelling Review – Business Card</title>
<link rel="stylesheet" href="https://fonts.googleapis.com/css2?family=Source+Sans+3:ital,wght@0,400;0,600;0,700;1,400&display=swap">
<style>
  :root {
    --backdrop: #3b3b3b;
    --card: #f8f8f8;
    --brown: #8e6b43;
    --orange: #f08a1c;
    --ink-light: #ffffff;
    --ink-grey: #4a4a4a;
  }
  * { box-sizing: border-box; margin: 0; padding: 0; }
  html, body {
    width: 1200px; height: 750px; overflow: hidden;
    background: var(--backdrop);
    font-family: "Source Sans 3", sans-serif;
  }
  .card {
    position: absolute; top: 228px;
    width: 461px; height: 262px;
    background: var(--card);
    overflow: hidden;
  }
  .card--front { left: 124px; }
  .card--back { left: 618px; }

  .swoosh { position: absolute; inset: 0; width: 100%; height: 100%; }

  .brand {
    position: absolute; left: 34px; top: 68px;
    display: flex; align-items: center; gap: 8px;
  }
  .brand__mark { width: 12px; height: 12px; background: var(--orange); }
  .brand__name {
    font-size: 18px; font-weight: 700; color: var(--brown); letter-spacing: 0.2px;
  }

  .contact {
    position: absolute; right: 33px; top: 89px;
    text-align: right; color: var(--ink-light);
  }
  .contact__name { font-size: 16.5px; font-weight: 600; color: var(--orange); line-height: 1.1; }
  .contact__role { font-size: 13px; line-height: 1.4; margin-bottom: 9px; }
  .contact__address { font-size: 11px; line-height: 1.3; font-style: normal; margin-bottom: 10px; }
  .contact__list { list-style: none; font-size: 11px; }
  .contact__list li {
    display: flex; justify-content: flex-end; align-items: center;
    gap: 9px; height: 17.6px;
  }
  .contact__list svg { width: 12px; height: 12px; fill: var(--orange); }

  .back-brand {
    position: absolute; left: 0; right: 0; top: 100px;
    display: flex; justify-content: center; align-items: center; gap: 12px;
  }
  .back-brand__mark { width: 18px; height: 18px; background: var(--orange); }
  .back-brand__name { font-size: 28px; font-weight: 700; color: var(--brown); }

  .services {
    position: absolute; left: 0; right: 0; top: 200px;
    text-align: center; font-style: italic; font-size: 11.8px;
    line-height: 17.6px; color: var(--ink-grey);
  }
  .services__dot { color: var(--orange); font-style: normal; }
</style>
</head>
<body>
  <section class="card card--front">
    <svg class="swoosh" viewBox="0 0 576 328" preserveAspectRatio="none" aria-hidden="true">
      <path d="M0,328 C190,215 370,70 495,68 C535,68 562,85 576,102 L576,328 Z" fill="var(--brown)"/>
      <path d="M6,320 C190,205 360,62 485,60 C528,59 560,72 576,88" fill="none" stroke="var(--orange)" stroke-width="3.5"/>
    </svg>

    <div class="brand">
      <span class="brand__mark"></span>
      <span class="brand__name">Brisket Dwelling Review</span>
    </div>

    <div class="contact">
      <p class="contact__name">Dana Whitlow</p>
      <p class="contact__role">CEO/Founder</p>
      <address class="contact__address">4120 Larkfield Road<br>Juniper, Oregon 61893</address>
      <ul class="contact__list">
        <li>541 208 7763
          <svg viewBox="0 0 24 24"><path d="M6.6 10.8a15.1 15.1 0 0 0 6.6 6.6l2.2-2.2a1 1 0 0 1 1-.25 11.4 11.4 0 0 0 3.6.57 1 1 0 0 1 1 1V20a1 1 0 0 1-1 1A17 17 0 0 1 3 4a1 1 0 0 1 1-1h3.5a1 1 0 0 1 1 1c0 1.25.2 2.45.57 3.57a1 1 0 0 1-.25 1z"/></svg>
        </li>
        <li>541 208 7764
          <svg viewBox="0 0 24 24"><path d="M7 3h10v5H7zM4 9h16a2 2 0 0 1 2 2v6h-4v4H6v-4H2v-6a2 2 0 0 1 2-2zm4 7v3h8v-3z"/></svg>
        </li>
        <li>mail@bdreview.com
          <svg viewBox="0 0 24 24"><path d="M2 5h20v14H2zm2 2v.5l8 5 8-5V7z"/></svg>
        </li>
        <li>www.bdreview.com
          <svg viewBox="0 0 24 24"><circle cx="12" cy="12" r="10"/></svg>
        </li>
      </ul>
    </div>
  </section>

  <section class="card card--back">
    <div class="back-brand">
      <span class="back-brand__mark"></span>
      <span class="back-brand__name">Brisket Dwelling Review</span>
    </div>
    <p class="services">
      Residential appraisals <span class="services__dot">•</span> Home inspection<br>
      Pest inspection and radon gas measurement.
    </p>
  </section>
</body>
</html>
```